Namecard design for Forex trading & training company

We need a design for a financial forex trading company.
Namecard should give customer a professional yet premium feel, able to differentiate from others.
1) most financial companies employs white background, while its clean and professional, it is too mainstream.
2) I am thinking of brown as base colour, however it easily gives the perception of being an Interior Design company
3) Task is to find a design that is able to portray a clean professional feel, at the same time, appear premium and differentiated from others.
*I'll be employing 3D textured print for my company namecard just so as to give it a better finishing.
Please find attached for my logo.
Financial

```html
<!DOCTYPE html>
<html lang="en">
<head>
<meta charset="utf-8">
<title>Velmora Capital – Business Cards</title>
<link rel="stylesheet" href="https://fonts.googleapis.com/css2?family=Lato:wght@400;700&display=swap">
<style>
  :root {
    --stage: #2e2e30;
    --card-white: #f6f6f6;
    --navy: #1f2f7a;
    --royal-blue: #2c3f99;
    --accent-red: #d2343c;
    --charcoal: #3b3b3d;
    --sky: #7ec8ef;
    --soft-white: #e9ecf6;
    --grey-text: #c9c9cc;
  }
  * { margin: 0; padding: 0; box-sizing: border-box; }
  html, body {
    width: 1200px; height: 997px; overflow: hidden;
    background: var(--stage);
    font-family: "Lato", "Helvetica Neue", Arial, sans-serif;
  }
  .stage {
    position: relative; width: 1200px; height: 997px;
    display: flex; flex-direction: column; align-items: center; justify-content: center; gap: 70px;
  }
  .card {
    position: relative; width: 640px; height: 366px;
    background: var(--card-white); overflow: hidden;
    box-shadow: 0 18px 40px rgba(0,0,0,0.45);
  }
  .card-curve { position: absolute; inset: 0; }
  .brand {
    position: absolute; left: 0; right: 0; top: 110px;
    display: flex; align-items: center; justify-content: center; gap: 14px;
    color: var(--navy); font-weight: 700; font-size: 28px; letter-spacing: 0.28em;
    text-transform: uppercase; line-height: 1;
  }
  .brand-dot { width: 16px; height: 16px; border-radius: 50%; background: var(--navy); }
  .card--back .brand { color: var(--charcoal); }
  .card--back .brand-dot { background: var(--charcoal); }
  .website {
    position: absolute; right: 50px; bottom: 44px;
    color: var(--grey-text); font-size: 18px; letter-spacing: 0.14em;
  }
  .contact-list {
    position: absolute; right: 30px; top: 232px;
    list-style: none; text-align: right; color: var(--soft-white);
    font-size: 16px; line-height: 1.2;
  }
  .contact-list li {
    display: flex; align-items: center; justify-content: flex-end; gap: 12px; margin-bottom: 10px;
  }
  .contact-list svg { width: 16px; height: 16px; fill: var(--sky); flex: none; }
  .person { position: absolute; left: 26px; bottom: 30px; }
  .person-name { color: #ffffff; font-size: 25px; font-weight: 700; display: flex; align-items: center; gap: 8px; line-height: 1.2; }
  .person-name::before {
    content: ""; width: 0; height: 0;
    border-top: 9px solid transparent; border-bottom: 9px solid transparent;
    border-left: 12px solid var(--sky);
  }
  .person-title { color: var(--sky); font-size: 19px; margin-left: 20px; line-height: 1.3; }
</style>
</head>
<body>
<main class="stage">

  <section class="card card--back" aria-label="Business card back">
    <svg class="card-curve" viewBox="0 0 640 366" preserveAspectRatio="none" aria-hidden="true">
      <path d="M0,290 Q360,310 640,120 L640,366 L0,366 Z" fill="var(--charcoal)"/>
      <path d="M0,290 Q360,310 640,120" fill="none" stroke="var(--accent-red)" stroke-width="3"/>
    </svg>
    <div class="brand"><span class="brand-dot"></span>Velmora Capital</div>
    <p class="website">www.velmoracapital.com</p>
  </section>

  <section class="card card--front" aria-label="Business card front">
    <svg class="card-curve" viewBox="0 0 640 366" preserveAspectRatio="none" aria-hidden="true">
      <path d="M0,230 Q330,290 640,60 L640,366 L0,366 Z" fill="var(--royal-blue)"/>
      <path d="M0,230 Q330,290 640,60" fill="none" stroke="var(--accent-red)" stroke-width="3"/>
    </svg>
    <div class="brand"><span class="brand-dot"></span>Velmora Capital</div>

    <ul class="contact-list">
      <li>+852 5550 1234
        <svg viewBox="0 0 16 16" aria-hidden="true"><path d="M4 0h8a1 1 0 0 1 1 1v14a1 1 0 0 1-1 1H4a1 1 0 0 1-1-1V1a1 1 0 0 1 1-1zm1 2v10h6V2H5zm3 11a1 1 0 1 0 0 2 1 1 0 0 0 0-2z"/></svg>
      </li>
      <li>enquiries@velmoracapital.com
        <svg viewBox="0 0 16 16" aria-hidden="true"><path d="M0 3h16v10H0V3zm1.5 1L8 9l6.5-5h-13z"/></svg>
      </li>
      <li>Harbor Tower F12-30, Pearl Bay
        <svg viewBox="0 0 16 16" aria-hidden="true"><path d="M8 0a5.5 5.5 0 0 0-5.5 5.5C2.5 10 8 16 8 16s5.5-6 5.5-10.5A5.5 5.5 0 0 0 8 0zm0 8a2.5 2.5 0 1 1 0-5 2.5 2.5 0 0 1 0 5z"/></svg>
      </li>
    </ul>

    <div class="person">
      <p class="person-name">Daniel Hale</p>
      <p class="person-title">Chief Executive Officer</p>
    </div>
  </section>

</main>
</body>
</html>
```